bottle label/ product label for smoothies (ultra fresh)

Please create a bottle label for our smoothies for retail distribution.
It's important that the following key features are clearly stated:

Ultra-fresh

Handmade

No preservatives

Not heat-treated

No added sugar

The base of the product label should be transparent, so that the color and content of the smoothie can be seen clearly.

We are a young, dynamic company. Our values are honesty, ultra-freshness, and authenticity — and we are the only ones producing this type of product in our country. We are positioned in the premium segment.

Design style: Modern, clean, and natural — but not playful or childish.

Example product: Selu Vane (Mango, Pineapple, Lemon, Passion Fruit, Orange)

Wenn du möchtest, kann ich auch gleich einen konkreten Vorschlag für das Etikettendesign auf Englisch oder einen Entwurfstext für das Label selbst erstellen. Sag einfach Bescheid!

Target Market(s)

trade - convenience

Industry/Entity Type

trade

Font styles to use
Sans Serif

Requirements
Must have
• sales- features: Ultra-fresh Handmade No preservatives Not heat-treated No added sugar

```html
<!DOCTYPE html>
<html lang="en">
<head>
<meta charset="utf-8">
<title>Veyra Selu Vane Smoothie Label</title>
<link href="https://fonts.googleapis.com/css2?family=Montserrat:wght@400;500;600&family=Dancing+Script:wght@700&display=swap" rel="stylesheet">
<style>
  :root {
    --canvas: #ffffff;
    --label: #f0c08a;
    --label-edge: #eab77c;
    --ink: #1c1a17;
    --fruit: #e9a85f;
  }
  html, body {
    margin: 0;
    padding: 0;
    width: 933px;
    height: 1200px;
    overflow: hidden;
    background: var(--canvas);
  }
  .canvas {
    position: relative;
    width: 933px;
    height: 1200px;
  }
  .label {
    position: absolute;
    left: 146px;
    top: 122px;
    width: 640px;
    height: 955px;
    border-radius: 30px;
    background: var(--label);
    box-shadow: inset 0 0 0 1px var(--label-edge);
    color: var(--ink);
    font-family: "Montserrat", Arial, sans-serif;
  }
  .brand {
    position: absolute;
    top: 72px;
    left: 0;
    width: 100%;
    text-align: center;
    font-weight: 600;
    font-size: 118px;
    line-height: 1;
    letter-spacing: -1px;
    margin: 0;
  }
  .fruit-mark {
    position: absolute;
    top: 246px;
    left: 285px;
    width: 70px;
    height: 76px;
    border-radius: 50% 50% 48% 52% / 58% 58% 42% 42%;
    background: var(--fruit);
  }
  .product-name {
    position: absolute;
    top: 370px;
    width: 100%;
    text-align: center;
    font-family: "Dancing Script", cursive;
    font-weight: 700;
    font-size: 96px;
    line-height: 1;
    margin: 0;
  }
  .flavour {
    position: absolute;
    top: 510px;
    width: 100%;
    text-align: center;
    font-size: 50px;
    font-weight: 500;
    line-height: 1;
    margin: 0;
  }
  .features {
    position: absolute;
    top: 650px;
    left: 0;
    width: 100%;
    height: 140px;
    margin: 0;
    padding: 0;
    list-style: none;
  }
  .feature {
    position: absolute;
    top: 0;
    width: 124px;
    margin-left: -62px;
    text-align: center;
    font-size: 15px;
    line-height: 1.2;
  }
  .feature svg {
    display: block;
    width: 92px;
    height: 92px;
    margin: 0 auto 16px;
  }
  .claim {
    position: absolute;
    top: 852px;
    width: 100%;
    text-align: center;
    font-size: 23px;
    font-weight: 500;
    line-height: 1.4;
    letter-spacing: 0.5px;
    margin: 0;
  }
</style>
</head>
<body>
<div class="canvas">
  <section class="label">
    <h1 class="brand">Veyra</h1>
    <div class="fruit-mark" role="img" aria-label="Small line illustration of a mango"></div>
    <h2 class="product-name">Selu Vane</h2>
    <p class="flavour">Mango</p>

    <ul class="features">
      <li class="feature" style="left:84px">
        <svg viewBox="0 0 92 92" fill="none" stroke="#1c1a17" stroke-width="3">
          <circle cx="46" cy="46" r="43"/>
          <path d="M46 22 C62 34 62 56 46 70 C30 56 30 34 46 22 Z"/>
          <path d="M46 34 V76"/>
        </svg>
        Ultra-fresh
      </li>
      <li class="feature" style="left:202px">
        <svg viewBox="0 0 92 92" fill="none" stroke="#1c1a17" stroke-width="3">
          <circle cx="46" cy="46" r="43"/>
          <path d="M20 56 C30 60 36 70 46 70 C56 70 62 60 72 56"/>
          <circle cx="46" cy="40" r="11"/>
        </svg>
        Handmade
      </li>
      <li class="feature" style="left:320px">
        <svg viewBox="0 0 92 92" fill="none" stroke="#1c1a17" stroke-width="3">
          <circle cx="46" cy="46" r="43"/>
          <text x="46" y="60" text-anchor="middle" fill="#1c1a17" stroke="none" font-family="Montserrat, Arial, sans-serif" font-weight="600" font-size="34">NO</text>
          <path d="M46 14 V26"/>
        </svg>
        No preservatives
      </li>
      <li class="feature" style="left:439px">
        <svg viewBox="0 0 92 92" fill="none" stroke="#1c1a17" stroke-width="3">
          <circle cx="46" cy="46" r="43"/>
          <path d="M26 58 H66 M30 48 C36 42 40 54 46 48 C52 42 56 54 62 48"/>
          <path d="M18 18 L74 74 M74 18 L18 74"/>
        </svg>
        Not heat-treated
      </li>
      <li class="feature" style="left:557px">
        <svg viewBox="0 0 92 92" fill="none" stroke="#1c1a17" stroke-width="3">
          <circle cx="46" cy="46" r="43"/>
          <rect x="30" y="30" width="32" height="32"/>
          <path d="M18 18 L74 74 M74 18 L18 74"/>
        </svg>
        No added sugar
      </li>
    </ul>

    <p class="claim">PREMIUM SMOOHIE<br>UNIQUE IN OUR COUNTRY</p>
  </section>
</div>
</body>
</html>
```